Business Card for Voltrix

Horizontal business card for voltrix, the electrical contractor.
clean and professional looking, using company branding and colours.
I also want the blue in the logo and wording to be made a more 'electric' blue and the grey 'Voltrix' to be slightly darker.

Pleas use the following contact details:

Colin Marsh
Owner

t: 01736 582910
m: 07831 206719
e: colin@voltrix-installs.co.uk

www.voltrix-installs.co.uk

Industry/Entity Type

Electrical

Font styles to use
Sans Serif

```html
<!DOCTYPE html>
<html lang="en">
<head>
<meta charset="utf-8">
<title>Voltrix – Business Card</title>
<link rel="stylesheet" href="https://fonts.googleapis.com/css2?family=Questrial&display=swap">
<style>
  :root {
    --page-bg: #f2f2f2;
    --card-white: #ffffff;
    --card-white-shade: #ececec;
    --card-dark: #26282b;
    --card-dark-deep: #17181a;
    --electric-blue: #1e6bff;
    --brand-grey: #45474a;
    --text-light: #f4f4f4;
    --text-muted: #d8d8d8;
  }
  * { box-sizing: border-box; margin: 0; padding: 0; }
  html, body {
    width: 1200px;
    height: 900px;
    overflow: hidden;
    background: var(--page-bg);
    font-family: "Questrial", "Century Gothic", sans-serif;
  }
  .stage {
    position: relative;
    width: 1200px;
    height: 900px;
    display: flex;
    align-items: center;
    justify-content: center;
    gap: 40px;
  }
  .card {
    position: relative;
    width: 540px;
    height: 308px;
    border-radius: 22px;
    overflow: hidden;
    box-shadow: 0 18px 30px rgba(0,0,0,0.18), 0 2px 6px rgba(0,0,0,0.12);
  }

  /* Front */
  .card-front {
    background: linear-gradient(180deg, var(--card-dark) 0%, var(--card-dark-deep) 100%);
  }
  .front-header {
    position: absolute;
    left: 0; top: 0;
    width: 100%;
    height: 146px;
    background: linear-gradient(180deg, var(--card-white) 0%, var(--card-white-shade) 100%);
  }
  .brand {
    position: absolute;
    left: 28px;
    top: 44px;
    display: flex;
    align-items: center;
    gap: 14px;
  }
  .brand-dot {
    width: 46px;
    height: 46px;
    border-radius: 50%;
    background: var(--electric-blue);
    flex: none;
  }
  .brand-text { display: flex; flex-direction: column; }
  .brand-name {
    font-size: 50px;
    line-height: 1;
    letter-spacing: 0.2em;
    color: var(--brand-grey);
  }
  .brand-tagline {
    margin-top: 6px;
    font-size: 19px;
    letter-spacing: 0.03em;
    color: var(--electric-blue);
  }
  .accent-stripe {
    position: absolute;
    left: 0; top: 146px;
    width: 100%;
    height: 13px;
    background: var(--electric-blue);
  }
  .contact {
    position: absolute;
    left: 26px;
    top: 172px;
    color: var(--text-light);
  }
  .contact-name {
    font-size: 20px;
    color: var(--electric-blue);
    line-height: 1.1;
  }
  .contact-role {
    font-size: 14px;
    color: var(--text-muted);
    margin-bottom: 16px;
  }
  .contact-line {
    display: flex;
    align-items: center;
    gap: 6px;
    font-size: 17px;
    line-height: 22px;
  }
  .contact-icon { width: 15px; height: 15px; flex: none; fill: var(--electric-blue); }

  /* Back */
  .card-back {
    background: linear-gradient(180deg, var(--card-dark) 0%, var(--card-dark-deep) 100%);
    display: flex;
    align-items: center;
    justify-content: center;
  }
  .back-ring {
    position: absolute;
    width: 230px;
    height: 230px;
    left: 50%;
    top: 50%;
    transform: translate(-50%, -50%);
    border-radius: 50%;
    background: rgba(255,255,255,0.04);
  }
  .website {
    position: relative;
    font-size: 19px;
    letter-spacing: 0.3em;
    color: var(--electric-blue);
  }
</style>
</head>
<body>
<main class="stage">
  <section class="card card-front" aria-label="Business card front">
    <div class="front-header">
      <div class="brand">
        <span class="brand-dot" aria-hidden="true"></span>
        <div class="brand-text">
          <span class="brand-name">VOLTRIX</span>
          <span class="brand-tagline">THE ELECTRICAL CONTRACTOR</span>
        </div>
      </div>
    </div>
    <div class="accent-stripe"></div>
    <div class="contact">
      <p class="contact-name">Colin Marsh</p>
      <p class="contact-role">Owner</p>
      <p class="contact-line">
        <svg class="contact-icon" viewBox="0 0 24 24" aria-hidden="true"><path d="M6.6 10.8a15.1 15.1 0 0 0 6.6 6.6l2.2-2.2a1 1 0 0 1 1-.25 11.4 11.4 0 0 0 3.6.57 1 1 0 0 1 1 1V20a1 1 0 0 1-1 1A17 17 0 0 1 3 4a1 1 0 0 1 1-1h3.5a1 1 0 0 1 1 1c0 1.25.2 2.45.57 3.57a1 1 0 0 1-.25 1z"/></svg>
        01736 582910
      </p>
      <p class="contact-line">
        <svg class="contact-icon" viewBox="0 0 24 24" aria-hidden="true"><path d="M7 1h10a2 2 0 0 1 2 2v18a2 2 0 0 1-2 2H7a2 2 0 0 1-2-2V3a2 2 0 0 1 2-2zm0 3v14h10V4z"/></svg>
        07831 206719
      </p>
      <p class="contact-line">
        <svg class="contact-icon" viewBox="0 0 24 24" aria-hidden="true"><path d="M2 5h20v14H2zm2 2v.5l8 5 8-5V7l-8 5z"/></svg>
        colin@voltrix-installs.co.uk
      </p>
    </div>
  </section>

  <section class="card card-back" aria-label="Business card back">
    <div class="back-ring" aria-hidden="true"></div>
    <p class="website">www.voltrix-installs.co.uk</p>
  </section>
</main>
</body>
</html>
```